Vitalune - Label design for a supplement with probiotic and prebiotic

Hello, we are a supplement company and we need a label design for our first product. The product's name is Vitalune and the company's name is Koravex Nutrition (Logo attached, It is allowed to change the color) and we are located in Orlando, if we like the label, in the future we can make other products too.
Our product is a supplement that contains probiotics, prebiotics and other vitamins, it will be packaged in a 300g plastic jar (Img attached), we like simple but premium-looking packaging.
Below are some links to brands and products we like:
https://www.shopvarelt.example/stores/page/7D1188AA-5521-4E9B-B302-B1A447FE22CC?ingress=2&visitId=91b2ccd4-774e-408a-bb21-c4e8f1aa2093&ref_=bl_dp_s_web_58213044022
https://www.shopvarelt.example/stores/page/61AB4E3D-92C1-4A77-9D20-7EE350173B81?ingress=2&visitId=8812fa0e-311c-4d2a-a7f4-1b9c30e44f12&ref_=bl_dp_s_web_24417720933
https://www.shopvarelt.example/stores/Teluvo+Nutrition/page/C2288340-5E61-4B19-93A4-12307C88D29E?store_ref=SLP_FW_450D77AB-C12E-4A98-A31F-2207E5C9A611
https://www.shopvarelt.example/stores/page/AA2C46DE-71F9-4B22-C390-5EEDC81B309F?ingress=2&visitId=15e93b27-6a0c-4f3e-9bd1-a7c2301ee9b4&ref_=bl_dp_s_web_4182930055
https://www.shopvarelt.example/stores/node/39527164022?_encoding=UTF8&field-lbr_brands_browse-bin=QUILMAXNUTRITION&ref_=bl_dp_s_web_39527164022
https://www.shopvarelt.example/stores/page/2B3E8804-6611-4C2A-9F17-E8A913B02C57?ingress=6&visitId=4461d09c-b12a-4d7e-8fa1-09c5d3e6bb21&store_ref=storeRecs_Instant_27316488033
Updates
Hi, This product will be packaged in a 300g bottle, it is allowed to insert images and it is very important to inform "100 Billion live bacteria", 5 grams of probiotic, 5 grams of prebiotic and orange flavor.
The bottle is rounded, the size of the art must be 2.87 in and 10.74 in, I will need barcode space, supplement facts, directions and warning. This information I can put later.
Target Market(s)
Our target is people who wish to have a healthier recovery after undergoing cancer treatments, helping to maintain health, improving quality of life and reducing the harm that these treatments cause.
Requirements
Must have
- It is very important that the product contains the following information:
- 100 Billion live bacteria
- 5 grams of probiotic and 5 grams of prebiotic
- No artificial flavours
- Space for barcode
Amount per container: 10.6 oz (300 g)
Serving size: 1 scoop (10 grams)
Servings per container: 30
Amount per serving
Calories 15 Calories from fat 0
Total Fat 0
Total Carbohydrate 5g
Dietary fiber 4g
Sugars 1g
Protein 0g
Proprietary Probiotic blend: 5 billons
Lactobacillus acidophilus
Bifidobacterium animalis subsp. lactis.
Other ingredients: Organic inulin fiber, stevia, natural orange flavor, citric acid, riboflavin Not a significant source of cholesterol, fat and protein
Nice to have
- We like simple design
Should not have
- Images from brolen photos.

```html
<!DOCTYPE html>
<html lang="en">
<head>
<meta charset="utf-8">
<title>Vitalune Label</title>
<link rel="stylesheet" href="https://fonts.googleapis.com/css2?family=Bebas+Neue&family=Oswald:wght@300;400&display=swap">
<style>
  :root {
    --teal: #0bc3b4;
    --ink: #1f1f22;
    --white: #ffffff;
    --page: #eceff3;
    --line: rgba(255,255,255,0.8);
    --icon-fill: rgba(255,255,255,0.22);
  }
  * { margin: 0; padding: 0; box-sizing: border-box; }
  html, body { width: 1200px; height: 920px; overflow: hidden; background: var(--page); }
  .canvas { position: relative; width: 1200px; height: 920px; }
  .label {
    position: absolute; left: 40px; top: 308px;
    width: 1344px; height: 364px;
    transform: scale(0.8333); transform-origin: 0 0;
    background: var(--white);
    box-shadow: 0 6px 16px rgba(0,0,0,0.18);
    overflow: hidden;
  }
  .label-shapes { position: absolute; inset: 0; }
  .barcode-space { position: absolute; left: 44px; top: 12px; width: 150px; height: 86px; background: var(--white); }

  .brand-line {
    position: absolute; left: 0; width: 1344px; top: 34px;
    display: flex; align-items: center; justify-content: center; gap: 8px;
    font: 400 18px/1 "Oswald", sans-serif; letter-spacing: 2px; text-transform: uppercase;
    color: var(--teal);
  }
  .brand-mark { width: 10px; height: 10px; background: var(--teal); }
  .product-name {
    position: absolute; left: 0; width: 1344px; top: 60px; text-align: center;
    font: 400 78px/1 "Bebas Neue", sans-serif; color: var(--ink); letter-spacing: 1px;
  }

  .facts, .ingredients {
    position: absolute; color: var(--white);
    font: 300 10.6px/13px "Oswald", sans-serif; letter-spacing: -0.1px;
  }
  .facts { left: 44px; top: 168px; }
  .ingredients { left: 234px; top: 261px; width: 110px; }

  .claims { position: absolute; left: 496px; top: 190px; display: flex; align-items: flex-end; }
  .claim { text-align: center; color: var(--white); font-family: "Bebas Neue", sans-serif; }
  .claim-icon { height: 58px; display: flex; align-items: center; justify-content: center; }
  .icon-spot { width: 40px; height: 40px; border-radius: 50%; background: var(--icon-fill); }
  .claim-figure { font-size: 29px; line-height: 26px; margin-top: 8px; }
  .claim-text { font-size: 13.5px; line-height: 13.5px; letter-spacing: 0.2px; }
  .claim-text.tight { letter-spacing: -0.3px; font-size: 12.5px; }
  .claim-billion { width: 96px; }
  .claim-grams { width: 136px; border-left: 1px solid var(--line); border-right: 1px solid var(--line); }
  .claim-flavour { width: 88px; }

  .burst-decoration {
    position: absolute; right: 0; bottom: 0; width: 340px; height: 150px;
    background: radial-gradient(ellipse at 50% 100%, rgba(255,255,255,0.55), rgba(255,255,255,0.12) 55%, rgba(255,255,255,0) 75%);
  }
</style>
</head>
<body>
<main class="canvas">
  <section class="label">
    <svg class="label-shapes" width="1344" height="364" viewBox="0 0 1344 364" aria-hidden="true">
      <polygon fill="var(--teal)" points="0,0 380,0 322,122 0,122"/>
      <polygon fill="var(--teal)" points="944,0 1344,0 1344,122 998,122"/>
      <polygon fill="var(--teal)" points="0,147 402,147 427,170 510,170 534,147 784,147 807,170 894,170 917,147 1344,147 1344,364 0,364"/>
    </svg>

    <div class="barcode-space"></div>

    <div class="brand-line"><span class="brand-mark"></span>Koravex Nutrition</div>
    <h1 class="product-name">VITALUNE</h1>

    <div class="facts">
      Amount per container: 10.6 oz (300 g)<br>
      Serving size: 1 scoop (10 grams)<br>
      Servings per container: 30<br>
      Amount per serving<br>
      Calories 15 Calories from fat 0<br>
      Total Fat 0<br>
      Total Carbohydrate 5g<br>
      Dietary fiber 4g<br>
      Sugars 1g<br>
      Protein 0g<br>
      Proprietary Probiotic blend: 5 billons<br>
      Lactobacillus acidophilus<br>
      Bifidobacterium animalis subsp. lactis.
    </div>

    <div class="ingredients">
      Other ingredients: Organic inulin fiber, stevia, natural orange flavor, citric acid, riboflavin Not a significant source of cholesterol, fat and protein
    </div>

    <div class="claims">
      <div class="claim claim-billion">
        <div class="claim-icon"><div class="icon-spot" role="img" aria-label="Icon of live bacteria"></div></div>
        <div class="claim-figure">100</div>
        <div class="claim-text">Billion<br>Live Bacteria</div>
      </div>

      <div class="claim claim-grams">
        <div class="claim-icon"><div class="icon-spot" role="img" aria-label="Icon of probiotic plus prebiotic"></div></div>
        <div class="claim-figure">5 Grams</div>
        <div class="claim-text tight">Of probiotic and 5<br>grams of prebiotic</div>
      </div>

      <div class="claim claim-flavour">
        <div class="claim-icon"><div class="icon-spot" role="img" aria-label="Icon for no artificial flavours"></div></div>
        <div class="claim-figure">No</div>
        <div class="claim-text">Artificial<br>Flavours</div>
      </div>
    </div>

    <div class="burst-decoration" role="img" aria-label="Decorative burst of white dots rising from the bottom edge"></div>
  </section>
</main>
</body>
</html>
```